Business card design needed

We are a gardening company who handle:
All Forms of gardens work including
Mowing
Pruning
edging
weeding
Poisoning
Landscaping
Minor Stump Removal
Rubbish Removal
and more

I want a card that look professional not cartoon style

Harlow Yards and Lawncare Service

Dean Marsholt
0486259041

```html
<!DOCTYPE html>
<html lang="en">
<head>
<meta charset="utf-8">
<title>Harlow Yards and Lawncare Service — Business Card</title>
<link rel="stylesheet" href="https://fonts.googleapis.com/css2?family=Quicksand:wght@300;400;700&display=swap">
<style>
  :root {
    --panel: #322d2b;
    --ink: #ffffff;
    --grass-light: #5fc04a;
    --grass-mid: #3a9a2e;
    --grass-deep: #1f6a1a;
  }
  html, body {
    margin: 0;
    padding: 0;
    width: 1200px;
    height: 693px;
    overflow: hidden;
    background: var(--panel);
  }
  .card {
    position: relative;
    width: 1200px;
    height: 693px;
    overflow: hidden;
    font-family: "Quicksand", sans-serif;
    color: var(--ink);
  }
  .info-panel {
    position: absolute;
    left: 0;
    top: 0;
    width: 873px;
    height: 693px;
    background: var(--panel);
  }
  .grass-photo {
    position: absolute;
    left: 873px;
    top: 0;
    width: 327px;
    height: 693px;
    background:
      linear-gradient(160deg, rgba(120,210,90,0.35) 0%, rgba(0,0,0,0) 40%),
      linear-gradient(180deg, var(--grass-mid) 0%, var(--grass-light) 30%, var(--grass-mid) 55%, var(--grass-light) 75%, var(--grass-deep) 100%);
  }
  .business-name {
    position: absolute;
    left: 33px;
    top: 71px;
    margin: 0;
    font-weight: 300;
    font-size: 65px;
    line-height: 85px;
    letter-spacing: 0.06em;
    white-space: nowrap;
  }
  .contact {
    position: absolute;
    left: 33px;
    top: 262px;
    margin: 0;
    font-weight: 300;
    font-size: 43px;
    line-height: 54px;
    letter-spacing: 0.06em;
    white-space: nowrap;
  }
  .contact .phone {
    font-weight: 700;
    margin-left: 6px;
  }
  .services {
    position: absolute;
    left: 35px;
    top: 495px;
    margin: 0;
  }
  .services-heading {
    margin: 0;
    font-weight: 700;
    font-size: 29px;
    line-height: 40px;
    letter-spacing: 0.07em;
  }
  .services-list {
    margin: 0;
    font-weight: 400;
    font-size: 26px;
    line-height: 34px;
    letter-spacing: 0.07em;
  }
  .services-list em {
    font-style: italic;
  }
</style>
</head>
<body>
  <div class="card">
    <section class="info-panel">
      <h1 class="business-name">Harlow Yards<br>and Lawncare Service</h1>
      <p class="contact">Dean Marsholt<span class="phone">0486259041</span></p>
      <div class="services">
        <p class="services-heading">All forms of garden work</p>
        <p class="services-list">including mowing, pruning, edging<br>weeding, poisoning, landscaping<br>minor stump removal, rubbish removal<br><em>and more</em></p>
      </div>
    </section>
    <div class="grass-photo" role="img" aria-label="Close-up photograph of long, wind-swept green grass"></div>
  </div>
</body>
</html>
```